Business Card Design

We are a trucking company that do a lot of business one on one with shippers. Our enthusiasm, honesty and hard work make us a great company to work with. We want to not only leave a lasting impression by the professionalism of our drivers but also give them something to remember us by for the future. I have a logo already designed that matches the same logo on the trucks. Its simple yet captures people to remember the name. We are expanding our coverage area by almost 700 miles and want to get our brand out there by having shippers call us to come back and conduct more business. I would like part of the logo itself raised but the shadowing not to give it a unique look and feel.
Industry/Entity Type
Trucking Company
Contact Information for Business Card
K&M Hauling LLC
Kurt & Melinda Ashcombe
402.618.2093 Kurt
402.551.4387 Melinda
kmhaulingllc@mailora.net

```html
<!DOCTYPE html>
<html lang="en">
<head>
<meta charset="utf-8">
<title>K&amp;M Hauling LLC – Business Card</title>
<link rel="stylesheet" href="https://fonts.googleapis.com/css2?family=Open+Sans:wght@400;700&display=swap">
<style>
  :root {
    --backdrop: #3b3d3f;
    --card-white: #ffffff;
    --card-sky: #b3d6ee;
    --stripe-navy: #1f2a86;
    --ink: #1a1a1a;
    --ink-soft: #2a2a2a;
  }
  * { box-sizing: border-box; margin: 0; padding: 0; }
  html, body {
    width: 791px;
    height: 1200px;
    overflow: hidden;
    background: var(--backdrop);
    font-family: "Open Sans", Verdana, sans-serif;
  }
  .canvas {
    position: relative;
    width: 791px;
    height: 1200px;
    display: flex;
    align-items: center;
    justify-content: center;
  }
  .business-card {
    position: relative;
    width: 700px;
    height: 400px;
    background: var(--card-sky);
    box-shadow: 0 10px 30px rgba(0,0,0,0.35);
    overflow: hidden;
  }
  .card-top {
    position: absolute;
    left: 0; top: 0;
    width: 100%;
    height: 192px;
    background: var(--card-white);
  }
  .card-stripe {
    position: absolute;
    left: 0; top: 192px;
    width: 100%;
    height: 11px;
    background: var(--stripe-navy);
  }
  .brand {
    position: absolute;
    left: 60px;
    top: 52px;
    display: flex;
    align-items: center;
    gap: 22px;
  }
  .brand-dot {
    width: 64px;
    height: 64px;
    border-radius: 50%;
    border: 4px solid var(--ink);
  }
  .brand-name {
    font-size: 28px;
    font-weight: 700;
    color: var(--ink);
    line-height: 1.1;
  }
  .brand-owners {
    font-size: 17px;
    font-weight: 400;
    color: var(--ink-soft);
    margin-top: 4px;
  }
  .contact-list {
    position: absolute;
    left: 258px;
    top: 240px;
    list-style: none;
  }
  .contact-item {
    display: flex;
    align-items: center;
    gap: 14px;
    font-size: 18px;
    color: var(--ink-soft);
    line-height: 1;
    margin-bottom: 13px;
  }
  .contact-icon {
    width: 16px;
    height: 18px;
    flex: none;
  }
</style>
</head>
<body>
<main class="canvas">
  <article class="business-card">
    <div class="card-top"></div>
    <div class="card-stripe"></div>

    <header class="brand">
      <span class="brand-dot" aria-hidden="true"></span>
      <div class="brand-text">
        <h1 class="brand-name">K&amp;M Hauling LLC</h1>
        <p class="brand-owners">CO Kurt &amp; Melinda Ashcombe</p>
      </div>
    </header>

    <ul class="contact-list">
      <li class="contact-item">
        <svg class="contact-icon" viewBox="0 0 16 18" aria-hidden="true">
          <rect x="3" y="1" width="10" height="16" rx="2" fill="#1a1a1a"/>
          <rect x="5" y="3" width="6" height="8" fill="#b3d6ee"/>
          <circle cx="8" cy="14" r="1.2" fill="#b3d6ee"/>
        </svg>
        <span>402 618 2093 Kurt</span>
      </li>
      <li class="contact-item">
        <svg class="contact-icon" viewBox="0 0 16 18" aria-hidden="true">
          <rect x="3" y="1" width="10" height="16" rx="2" fill="#1a1a1a"/>
          <rect x="5" y="3" width="6" height="8" fill="#b3d6ee"/>
          <circle cx="8" cy="14" r="1.2" fill="#b3d6ee"/>
        </svg>
        <span>402 551 4387 Melinda</span>
      </li>
      <li class="contact-item">
        <svg class="contact-icon" viewBox="0 0 16 18" aria-hidden="true">
          <rect x="1" y="4" width="14" height="10" fill="none" stroke="#1a1a1a" stroke-width="1.6"/>
          <polyline points="1,4 8,10 15,4" fill="none" stroke="#1a1a1a" stroke-width="1.6"/>
        </svg>
        <span>kmhaulingllc@mailora.net</span>
      </li>
    </ul>
  </article>
</main>
</body>
</html>
```